U.S. Popcorn company needs business cards

We are a popcorn company that manufactures popcorn and sells it to grocery stores worldwide. Our theme is "Americana" and our logo is U.S. route 66 which is the most famous highway in the U.S.

We would like the design to be simple and to use both sides. On the back side we would like to see just the logo and website. The front would be normal details

Target Market(s)

Wholesalers, grocers and distributors

Industry/Entity Type

Manufacture

Contact Information for Business Card

Business name: Bluebell Ridge Popcorn
Phone: +1 555 014 2286
Email: Derek@bluebellridgepopcorn.com
website: www.bluebellridgepopcorn.com
Tag Line: "POPular for a reason"
Name: Derek Halvorsen
Title: Founder/President

Requirements
Must have
• Either this design should be fun or clean and simple. I will let you show me your thougths.
Nice to have
• Anything that ties in the real Hwy Route 66.
• Colors might need to be red, white and blue incorporated.
Should not have
• Not be too busy.

```html
<!DOCTYPE html>
<html lang="en">
<head>
<meta charset="utf-8">
<title>Derek Halvorsen — Bluebell Ridge Popcorn</title>
<link rel="stylesheet" href="https://fonts.googleapis.com/css2?family=Zilla+Slab:wght@400;500&family=Exo+2:wght@300;400&display=swap">
<style>
  :root {
    --card-bg: #ffffff;
    --ink: #434343;
    --ink-soft: #4a4a4a;
    --popcorn-red: #f44336;
    --divider-pink: #e8909e;
  }
  * { margin: 0; padding: 0; box-sizing: border-box; }
  html, body {
    width: 1200px;
    height: 711px;
    overflow: hidden;
    background: var(--card-bg);
  }
  .card {
    position: relative;
    width: 1200px;
    height: 711px;
    background: var(--card-bg);
    overflow: hidden;
  }
  .popcorn-box {
    position: absolute;
    left: 435px;
    top: 0;
    width: 388px;
    height: 136px;
    background: var(--popcorn-red);
    border-radius: 0 0 12px 12px;
  }
  .name {
    position: absolute;
    left: 0;
    right: 0;
    top: 206px;
    text-align: center;
    font-family: "Zilla Slab", serif;
    font-weight: 400;
    font-size: 82px;
    line-height: 1;
    letter-spacing: 6px;
    color: var(--ink);
    text-transform: uppercase;
  }
  .role {
    position: absolute;
    left: 0;
    right: 0;
    top: 328px;
    text-align: center;
    font-family: "Zilla Slab", serif;
    font-weight: 400;
    font-size: 50px;
    line-height: 1;
    letter-spacing: 4px;
    color: var(--ink);
    text-transform: uppercase;
  }
  .divider {
    position: absolute;
    left: 492px;
    top: 432px;
  }
  .contact {
    position: absolute;
    left: 0;
    right: 0;
    top: 498px;
    text-align: center;
    font-family: "Exo 2", sans-serif;
    font-weight: 400;
    font-size: 32px;
    line-height: 48.5px;
    letter-spacing: 1px;
    color: var(--ink-soft);
    list-style: none;
  }
  .contact .company { text-transform: uppercase; letter-spacing: 2px; }
</style>
</head>
<body>
  <main class="card">
    <div class="popcorn-box" role="img" aria-label="Red and white striped popcorn box illustration"></div>

    <h1 class="name">Derek Halvorsen</h1>
    <p class="role">Founder/President</p>

    <svg class="divider" width="218" height="20" viewBox="0 0 218 20" aria-hidden="true">
      <g fill="var(--divider-pink)">
        <circle cx="9" cy="10" r="8"/>
        <circle cx="42" cy="10" r="8"/>
        <circle cx="75" cy="10" r="8"/>
        <circle cx="108" cy="10" r="8"/>
        <circle cx="141" cy="10" r="8"/>
        <circle cx="174" cy="10" r="8"/>
        <circle cx="207" cy="10" r="8"/>
      </g>
    </svg>

    <ul class="contact">
      <li class="company">Bluebell Ridge Popcorn</li>
      <li class="phone">+1 555 014 2286</li>
      <li class="email">Derek@bluebellridgepopcorn.com</li>
      <li class="website">www.bluebellridgepopcorn.com</li>
    </ul>
  </main>
</body>
</html>
```